Step repeat logo/Pull ups

Urgent Large Format Print Designer Needed — Today/Tomorrow

Hello, I need an experienced large-format print designer to redesign several event banners for my company, Harbellow Insurance Agency Inc.

I created the initial concepts using ChatGPT, but the files are not high enough quality for printing. I do not need someone to simply upscale the images. I need someone who can rebuild the designs professionally from scratch so they are clean, sharp, print-ready, and accepted by PlumeGrid or any professional printer.

This project is urgent. I need someone who is available today and tomorrow because I need these files completed ASAP in order to print and receive them on time.

We are designing approximately 7 pieces, including:

1. Step-and-repeat backdrop — 10 ft × 8 ft
2. Pull-up banners — 47 in × 81 in
3. Welcome banner
4. Sponsor thank-you banner
5. Brand values banner
6. Brand essence banner
7. Motivation / AEP Kick-Off event banners

The style must match our brand: professional, premium, clean, modern, corporate, inspiring, and high-quality. Our colors are navy, blue, purple, white, and gold accents.

Important requirements:

* Use the official Harbellow logo exactly as provided
* Do not recreate, redraw, distort, or modify the logo
* Text must be clean, readable, and print-sharp
* Final files must be built at the correct real print sizes
* Must include proper bleed and safe margins
* Must be print-ready for PlumeGrid or large-format printing
* Must provide editable source files
* Fonts must be outlined or included
* No blurry images
* No AI-looking letters
* No spelling mistakes
* No low-resolution graphics

Required final deliverables:

* Editable AI, EPS, or layered PDF source file
* Print-ready PDF
* High-resolution PNG
* JPG backup if possible
* All files sized correctly:
* Step backdrop: 10 ft × 8 ft
* Pull-ups: 47 in × 81 in

I already have the design direction, logo, colors, and examples. I need a designer who can take the concept and make it truly professional for print.

Please only apply if you have experience with large-format banners, step-and-repeat backdrops, pull-up banners, trade show graphics, and print production.

If you do not have time today or tomorrow, please do not apply.
If you do not know how to design at this level for professional printing, please do not apply.

Thank you.

Target Market(s)

Insurance Brokers Event/Motivational event

Colors
0054AA
0677BA
7BADD7
CADEEF
E8F1F8
0094D4
00A9DD
6FCCEA
C7EBF8
E9F6FB
6B429C
8869AF
B7A5CE
E3DAEB
F3F0F8

```html
<!DOCTYPE html>
<html lang="en">
<head>
<meta charset="utf-8">
<title>Harbellow Event Banners</title>
<link rel="stylesheet" href="https://fonts.googleapis.com/css2?family=Poppins:wght@500;600;800&family=EB+Garamond:ital,wght@0,500;0,700;1,400&display=swap">
<style>
:root{
  --stage:#4a4a4a;
  --white:#ffffff;
  --purple-dark:#4b2470;
  --purple:#8869AF;
  --purple-deep:#6B429C;
  --blue:#0094D4;
  --blue-sky:#3fa9e4;
  --blue-royal:#2c4fa0;
  --navy:#0c1637;
  --gold:#c99a3a;
  --gold-light:#e6c06a;
  --ink:#2a2245;
}
*{margin:0;padding:0;box-sizing:border-box}
html,body{width:757px;height:1200px;overflow:hidden;background:var(--stage)}
.stage{position:relative;width:757px;height:1200px}

/* shared name lockup */
.logo{position:absolute;text-align:center;transform:translateX(-50%)}
.logo-name{display:inline-flex;align-items:center;gap:.18em;font-family:"Poppins",sans-serif;font-weight:600;color:var(--purple-dark);font-size:var(--s);line-height:1.1;letter-spacing:-.01em}
.logo-name::before{content:"";width:.55em;height:.55em;border-radius:50%;background:var(--blue)}
.logo-tag{display:flex;align-items:center;gap:.5em;justify-content:center;margin-top:.35em;font-family:"EB Garamond",serif;font-weight:500;font-size:calc(var(--s)*.3);letter-spacing:.12em;color:var(--ink);white-space:nowrap}
.logo-tag::before,.logo-tag::after{content:"";flex:1;height:1px;background:var(--gold);min-width:1.6em}

/* step and repeat backdrop */
.backdrop{position:absolute;left:43px;top:38px;width:666px;height:533px;background:var(--white);overflow:hidden}
.corner-art{position:absolute;width:250px;height:150px}
.corner-art-top{left:0;top:0;background:linear-gradient(150deg,var(--purple-deep) 0%,var(--blue-royal) 30%,rgba(230,192,106,.45) 45%,rgba(255,255,255,0) 70%)}
.corner-art-bottom{right:0;bottom:0;background:linear-gradient(330deg,var(--purple-deep) 0%,var(--blue-royal) 30%,rgba(230,192,106,.45) 45%,rgba(255,255,255,0) 70%)}
.backdrop-frame{position:absolute;left:12px;top:11px;width:641px;height:509px;border:1.5px solid var(--gold)}
.values{position:absolute;transform:translateX(-50%);text-align:center;font-family:"EB Garamond",serif;font-style:italic;font-size:11.5px;line-height:1.3;color:var(--ink);white-space:nowrap}
.pillars{position:absolute;transform:translateX(-50%);text-align:center;font-family:"EB Garamond",serif;font-size:12px;line-height:1.2;color:var(--ink);white-space:nowrap}
.dot{color:var(--gold);padding:0 .2em}
.event-year{position:absolute;left:339px;top:218px;transform:translateX(-50%);font-family:"EB Garamond",serif;font-weight:700;font-size:50px;line-height:1.1;color:var(--purple-dark);white-space:nowrap;letter-spacing:-.01em}
.script-art{position:absolute;border-radius:4px}
.kickoff-art{left:256px;top:273px;width:165px;height:42px;background:linear-gradient(90deg,#b07f2a,var(--gold-light),#a87525)}
.event-date{position:absolute;left:338px;top:318px;transform:translateX(-50%);font-family:"EB Garamond",serif;font-weight:700;font-size:19px;line-height:1.2;color:var(--ink);white-space:nowrap}
.gold-rule{position:absolute;left:238px;top:347px;width:200px;height:1.5px;background:var(--gold)}
.event-motto{position:absolute;left:338px;top:352px;transform:translateX(-50%);font-family:"EB Garamond",serif;font-style:italic;font-size:15px;line-height:1.2;color:var(--ink);white-space:nowrap}
.personal-art-gold{left:266px;top:374px;width:147px;height:28px;background:linear-gradient(90deg,#a97a2c,var(--gold-light),#b5882f)}

/* pull-up banners */
.pullup{position:absolute;top:602px;width:325px;height:558px;overflow:hidden}
.pullup-values{left:43px;background:var(--navy)}
.pullup-essence{left:385px;background:linear-gradient(180deg,#161a3a,#0e1230 60%,#120f30)}
.pullup-shape{position:absolute;inset:0;width:100%;height:100%}
.headline{position:absolute;left:50%;transform:translateX(-50%);font-family:"Poppins",sans-serif;font-weight:800;line-height:1;white-space:nowrap;text-align:center}
.hl-white{color:var(--white)}
.hl-sky{color:var(--blue-sky)}
.hl-purple{color:var(--purple)}
.glow-rule{position:absolute;left:82px;width:160px;height:2px;background:linear-gradient(90deg,transparent,var(--blue-sky),transparent)}
.feature-row{position:absolute;left:0;top:400px;width:100%;display:flex}
.feature{flex:1;display:flex;flex-direction:column;align-items:center;gap:8px;font-family:"Poppins",sans-serif;font-weight:500;font-size:9.5px;color:var(--white);letter-spacing:.02em}
.feature+.feature{border-left:1px solid rgba(255,255,255,.25)}
.feature svg{width:26px;height:26px}
.pullup-motto{position:absolute;left:50%;top:498px;transform:translateX(-50%);font-family:"Poppins",sans-serif;font-weight:600;font-size:10.5px;color:var(--navy);white-space:nowrap}
.personal-art-blue{left:89px;top:516px;width:157px;height:28px;background:linear-gradient(90deg,#1f8ad4,#3fb4ea,#1e6fc0)}
.personal-art-large{left:30px;top:284px;width:268px;height:56px;background:linear-gradient(90deg,#a87828,var(--gold-light),#b98b34)}
.service-line{position:absolute;left:50%;top:356px;transform:translateX(-50%);font-family:"Poppins",sans-serif;font-weight:600;font-size:12px;color:var(--white);white-space:nowrap}
.city-art{position:absolute;left:0;top:376px;width:325px;height:182px;background:linear-gradient(180deg,#0f1a33 0%,#123645 40%,#2a2536 70%,#5a3040 100%)}
.closing{position:absolute;left:0;top:522px;width:100%;display:flex;align-items:center;gap:8px;padding:0 35px;font-family:"EB Garamond",serif;font-style:italic;font-size:10.5px;color:var(--white);white-space:nowrap}
.closing::before,.closing::after{content:"";flex:1;height:1px;background:var(--gold)}
</style>
</head>
<body>
<main class="stage">

  <section class="backdrop" aria-label="Step and repeat backdrop">
    <div class="corner-art corner-art-top" role="img" aria-label="Decorative purple, blue and gold flowing ribbons in the top left corner"></div>
    <div class="corner-art corner-art-bottom" role="img" aria-label="Decorative purple, blue and gold flowing ribbons in the bottom right corner"></div>
    <div class="backdrop-frame"></div>

    <div class="logo" style="left:327px;top:46px;--s:26px"><div class="logo-name">Harbellow</div><div class="logo-tag">AN ALDERWAY | PARTNER OFFICE</div></div>
    <div class="logo" style="left:127px;top:84px;--s:26px"><div class="logo-name">Harbellow</div><div class="logo-tag">AN ALDERWAY | PARTNER OFFICE</div></div>
    <div class="logo" style="left:537px;top:84px;--s:26px"><div class="logo-name">Harbellow</div><div class="logo-tag">AN ALDERWAY | PARTNER OFFICE</div></div>
    <div class="logo" style="left:336px;top:150px;--s:42px"><div class="logo-name">Harbellow</div><div class="logo-tag">AN ALDERWAY | PARTNER OFFICE</div></div>
    <div class="logo" style="left:110px;top:234px;--s:24px"><div class="logo-name">Harbellow</div><div class="logo-tag">AN ALDERWAY | PARTNER OFFICE</div></div>
    <div class="logo" style="left:555px;top:234px;--s:24px"><div class="logo-name">Harbellow</div><div class="logo-tag">AN ALDERWAY | PARTNER OFFICE</div></div>
    <div class="logo" style="left:110px;top:347px;--s:24px"><div class="logo-name">Harbellow</div><div class="logo-tag">AN ALDERWAY | PARTNER OFFICE</div></div>
    <div class="logo" style="left:548px;top:347px;--s:24px"><div class="logo-name">Harbellow</div><div class="logo-tag">AN ALDERWAY | PARTNER OFFICE</div></div>
    <div class="logo" style="left:162px;top:423px;--s:21px"><div class="logo-name">Harbellow</div><div class="logo-tag">AN ALDERWAY | PARTNER OFFICE</div></div>
    <div class="logo" style="left:341px;top:422px;--s:21px"><div class="logo-name">Harbellow</div><div class="logo-tag">AN ALDERWAY | PARTNER OFFICE</div></div>
    <div class="logo" style="left:527px;top:419px;--s:21px"><div class="logo-name">Harbellow</div><div class="logo-tag">AN ALDERWAY | PARTNER OFFICE</div></div>

    <p class="values" style="left:90px;top:165px">Integrity <span class="dot">•</span>Education <span class="dot">•</span><br>Opportunity <span class="dot">•</span>Community<span class="dot">•</span><br>Excellence</p>
    <p class="values" style="left:577px;top:165px">Integrity <span class="dot">•</span>Education <span class="dot">•</span><br>Opportunity <span class="dot">•</span>Community<span class="dot">•</span><br>Excellence</p>
    <p class="values" style="left:341px;top:466px">Integrity <span class="dot">•</span>Education <span class="dot">•</span><br>Opportunity <span class="dot">•</span>Community<span class="dot">•</span><br>Excellence</p>

    <p class="pillars" style="left:114px;top:292px">TOOLS <span class="dot">•</span>TRAINING <span class="dot">•</span><br>SUPPORT <span class="dot">•</span>GROWTH<span class="dot">•</span></p>
    <p class="pillars" style="left:556px;top:292px">TOOLS <span class="dot">•</span>TRAINING <span class="dot">•</span><br>SUPPORT <span class="dot">•</span>GROWTH<span class="dot">•</span></p>

    <h1 class="event-year">2027 AEP</h1>
    <div class="script-art kickoff-art" role="img" aria-label="Gold hand-lettered script reading Kick-off"></div>
    <p class="event-date">September 25,2026</p>
    <div class="gold-rule"></div>
    <p class="event-motto">Building Brokers . Serving Communities.</p>
    <div class="script-art personal-art-gold" role="img" aria-label="Gold brush lettering reading This Is Personal"></div>
  </section>

  <section class="pullup pullup-values" aria-label="Brand values pull-up banner">
    <svg class="pullup-shape" viewBox="0 0 325 558" preserveAspectRatio="none" aria-hidden="true">
      <defs>
        <linearGradient id="paper" x1="0" y1="0" x2="0" y2="1">
          <stop offset="0" stop-color="#ffffff"/><stop offset="1" stop-color="#e3e6f3"/>
        </linearGradient>
        <radialGradient id="side-glow" cx="0" cy=".5" r=".6">
          <stop offset="0" stop-color="#1e5fa8" stop-opacity=".55"/><stop offset="1" stop-color="#0c1637" stop-opacity="0"/>
        </radialGradient>
      </defs>
      <rect width="325" height="558" fill="#0c1637"/>
      <rect x="0" y="80" width="200" height="400" fill="url(#side-glow)"/>
      <path d="M0,0 H325 V85 C230,110 110,115 0,72 Z" fill="url(#paper)"/>
      <path d="M0,72 C110,115 230,110 325,85 V96 C230,122 110,126 0,84 Z" fill="#6B429C"/>
      <path d="M0,84 C110,126 230,122 325,96 V104 C230,132 110,134 0,94 Z" fill="#2a78d0"/>
      <path d="M0,478 C100,456 220,458 325,468 V462 C220,450 100,450 0,470 Z" fill="#2a78d0"/>
      <path d="M0,488 C100,466 220,468 325,478 V468 C220,458 100,456 0,478 Z" fill="#6B429C"/>
      <path d="M0,488 C100,466 220,468 325,478 V558 H0 Z" fill="url(#paper)"/>
    </svg>

    <div class="logo" style="left:162px;top:14px;--s:32px"><div class="logo-name">Harbellow</div><div class="logo-tag" style="font-family:'Poppins',sans-serif;font-size:9px;letter-spacing:.14em">AN ALDERWAY PARTNER OFFICE</div></div>

    <h2 class="headline hl-white" style="top:153px;font-size:28px">BUILD WITH</h2>
    <h2 class="headline hl-sky" style="top:181px;font-size:33px">INTEGRITY.</h2>
    <div class="glow-rule" style="top:225px"></div>
    <h2 class="headline hl-white" style="top:240px;font-size:28px">SERVE WITH</h2>
    <h2 class="headline hl-purple" style="top:268px;font-size:33px">PURPOSE.</h2>
    <div class="glow-rule" style="top:311px"></div>
    <h2 class="headline hl-white" style="top:322px;font-size:28px">GROW</h2>
    <h2 class="headline hl-sky" style="top:349px;font-size:33px">TOGETHER.</h2>

    <div class="feature-row">
      <div class="feature">
        <svg viewBox="0 0 24 24" fill="none" stroke="#3fa9e4" stroke-width="1.4"><circle cx="12" cy="12" r="3.5"/><circle cx="12" cy="12" r="7.5" stroke-dasharray="3 2"/></svg>
        TOOLS
      </div>
      <div class="feature">
        <svg viewBox="0 0 24 24" fill="none" stroke="#8869AF" stroke-width="1.4"><path d="M2,5 C6,4 10,4 12,6 C14,4 18,4 22,5 V19 C18,18 14,18 12,20 C10,18 6,18 2,19 Z"/><path d="M12,6 V20"/></svg>
        TRAINING
      </div>
      <div class="feature">
        <svg viewBox="0 0 24 24" fill="none" stroke="#3fa9e4" stroke-width="1.4"><circle cx="12" cy="8" r="3"/><circle cx="5.5" cy="9" r="2.3"/><circle cx="18.5" cy="9" r="2.3"/><path d="M6,20 C6,15 18,15 18,20 Z"/><path d="M1,19 C1,15 4,14 6,15"/><path d="M23,19 C23,15 20,14 18,15"/></svg>
        SUPPORT
      </div>
      <div class="feature">
        <svg viewBox="0 0 24 24" fill="none" stroke="#8869AF" stroke-width="1.4"><rect x="3" y="14" width="4" height="7"/><rect x="10" y="10" width="4" height="11"/><rect x="17" y="6" width="4" height="15"/><path d="M3,10 L10,5 L14,7 L21,2"/><path d="M17,2 H21 V6"/></svg>
        GROWTH
      </div>
    </div>

    <p class="pullup-motto">Building Brokers. Service Communities</p>
    <div class="script-art personal-art-blue" role="img" aria-label="Blue brush lettering reading This Is Personal"></div>
  </section>

  <section class="pullup pullup-essence" aria-label="Brand essence pull-up banner">
    <div class="logo" style="left:162px;top:18px;--s:32px"><div class="logo-name" style="color:var(--purple)">Harbellow</div><div class="logo-tag" style="color:var(--white);font-size:9.5px">AN ALDERWAY PARTNER OFFICE</div></div>

    <h2 class="headline hl-white" style="top:124px;font-size:33px">BUILDING</h2>
    <h2 class="headline hl-purple" style="top:157px;font-size:33px">BROKERS.</h2>
    <h2 class="headline hl-white" style="top:202px;font-size:33px">SERVICE</h2>
    <h2 class="headline hl-sky" style="top:234px;font-size:30px">COMMUNITIES.</h2>
    <div class="script-art personal-art-large" role="img" aria-label="Gold brush lettering reading This Is Personal with a swash underline"></div>
    <p class="service-line">Tools. Training. Support. Growth.</p>

    <div class="city-art" role="img" aria-label="Night city skyline with light trails on a highway"></div>
    <p class="closing">Because it’s personal to you.</p>
  </section>

</main>
</body>
</html>
```